Lowell Brandt

20 Year Licensed Master Barber specializing in:
men/women cuts, Grooming, Straight razor Shaving and tape line enhancement, beard grooming, eye brow enhancement, South of France, Hot Towel Treatments, Scalp, Blow outs, Shags, Custom Design,RazorCuts,Shear Cuts, Bobs, Perms, Relaxers, Shoe Shine.
Please create a wonderful business card incorporating all the info above and selecting one of the photos. Please be creative.

Barber

```html
<!DOCTYPE html>
<html lang="en">
<head>
<meta charset="utf-8">
<title>Lowell Brandt — Master Barber business card</title>
<link rel="stylesheet" href="https://fonts.googleapis.com/css2?family=Quicksand:wght@400;600;700&family=Lato:wght@400;700&display=swap">
<style>
  :root {
    --page: #e9e6e2;
    --card-black: #0b0b0d;
    --steel-mid: #8c8c92;
    --accent-red: #d21f2b;
    --accent-violet: #4b3fa6;
    --accent-violet-deep: #2c2480;
    --violet-soft: #6a5fd0;
    --text-light: #f2f2f2;
    --text-dim: #bdbdc4;
  }
  * { box-sizing: border-box; margin: 0; padding: 0; }
  html, body { width: 1200px; height: 1200px; overflow: hidden; }
  body {
    background: var(--page);
    position: relative;
    font-family: "Quicksand", sans-serif;
  }
  .card {
    position: absolute;
    top: 170px;
    width: 480px;
    height: 860px;
    background: var(--card-black);
    overflow: hidden;
    box-shadow: 0 14px 30px rgba(0,0,0,0.25);
  }
  .card--front { left: 90px; }
  .card--back { left: 630px; background: linear-gradient(160deg, #1b1b20 0%, var(--card-black) 45%); }

  /* Front */
  .portrait {
    position: absolute;
    left: 0; top: 0;
    width: 480px; height: 560px;
    background:
      radial-gradient(ellipse 42% 40% at 40% 42%, #5a5a5f 0%, #2c2c30 55%, transparent 80%),
      linear-gradient(180deg, #2a2a2e 0%, #1a1a1d 70%, var(--card-black) 100%);
  }
  .chevrons { position: absolute; left: 0; top: 180px; width: 480px; height: 440px; }
  .brand-mark {
    position: absolute;
    display: flex; align-items: center; gap: 10px;
    color: var(--text-light);
    font-family: "Quicksand", sans-serif;
    font-weight: 700;
    font-size: 20px;
  }
  .brand-mark__dot {
    width: 22px; height: 22px;
    border-radius: 50%;
    background: var(--accent-violet);
    flex: none;
  }
  .card--front .brand-mark { top: 40px; right: 30px; }
  .identity {
    position: absolute;
    left: 0; right: 0; top: 645px;
    padding: 0 36px;
    text-align: right;
  }
  .identity__name {
    font-family: "Quicksand", sans-serif;
    font-weight: 700;
    font-size: 46px;
    letter-spacing: 0.5px;
    color: var(--text-light);
    line-height: 1;
  }
  .identity__initial { color: var(--accent-red); }
  .identity__rule {
    height: 2px;
    margin: 12px 0 10px;
    background: linear-gradient(90deg, var(--accent-red), var(--accent-violet));
  }
  .identity__title {
    font-size: 20px;
    letter-spacing: 1px;
    color: var(--violet-soft);
    text-transform: uppercase;
    padding-right: 80px;
  }
  .contact {
    position: absolute;
    left: 0; right: 0; top: 770px;
    text-align: center;
    font-size: 20px;
    color: var(--text-dim);
    line-height: 1.9;
  }
  .contact__label { color: var(--accent-red); }

  /* Back */
  .social {
    position: absolute;
    top: 48px; left: 40px;
    font-family: "Lato", sans-serif;
    font-size: 20px;
    color: var(--text-light);
    list-style: none;
    line-height: 1.8;
  }
  .social__item { display: flex; align-items: center; gap: 10px; }
  .social__icon { width: 14px; height: 14px; background: var(--steel-mid); border-radius: 2px; }
  .card--back .brand-mark { top: 70px; right: 30px; }
  .services {
    position: absolute;
    top: 300px; left: 40px; right: 40px;
    font-family: "Lato", sans-serif;
    color: var(--text-light);
  }
  .services__intro {
    color: var(--violet-soft);
    font-size: 21px;
    line-height: 1.25;
    margin-bottom: 8px;
  }
  .services__list { list-style: none; font-size: 20px; line-height: 1.45; }
  .services__list li { display: flex; gap: 10px; align-items: baseline; }
  .services__list li::before {
    content: "";
    width: 6px; height: 12px;
    border-left: 2px solid var(--text-dim);
    border-right: 2px solid var(--text-dim);
    flex: none;
  }
  .services__list li.cont::before { border-color: transparent; }
  .sweep { position: absolute; left: 0; bottom: 0; width: 480px; height: 300px; }
</style>
</head>
<body>
  <section class="card card--front" aria-label="Business card front">
    <div class="portrait" role="img" aria-label="Portrait photo of the barber in a black tuxedo and bow tie against a dark brick wall"></div>
    <svg class="chevrons" viewBox="0 0 480 440" aria-hidden="true">
      <polygon points="0,120 55,120 235,435 180,435" fill="#9a9aa0" opacity="0.55"/>
      <polygon points="60,150 95,150 255,430 220,430" fill="#d9d9dc" opacity="0.5"/>
      <polygon points="420,40 470,40 285,430 240,430" fill="#c8c8cc" opacity="0.6"/>
      <polygon points="380,110 410,110 255,420 225,420" fill="#6f6f75" opacity="0.6"/>
    </svg>
    <div class="brand-mark"><span class="brand-mark__dot"></span>Lowell Brandt</div>
    <div class="identity">
      <h1 class="identity__name"><span class="identity__initial">L</span>OWELL BRANDT</h1>
      <div class="identity__rule"></div>
      <p class="identity__title">Master Barber</p>
    </div>
    <div class="contact">
      <p><span class="contact__label">P:</span> (555) 301-4418</p>
      <p><span class="contact__label">E:</span> lowell.brandt3@mailbox.com</p>
    </div>
  </section>

  <section class="card card--back" aria-label="Business card back">
    <ul class="social">
      <li class="social__item"><span class="social__icon"></span>lbcuts</li>
      <li class="social__item"><span class="social__icon"></span>Social/link</li>
    </ul>
    <div class="brand-mark"><span class="brand-mark__dot"></span>Lowell Brandt</div>
    <div class="services">
      <p class="services__intro">20 Year Licensed Master Barber<br>specializing in:</p>
      <ul class="services__list">
        <li>Men/women cuts</li>
        <li>Grooming</li>
        <li>Straight razor Shaving</li>
        <li class="cont">and tape line enhancement</li>
        <li>Beard grooming</li>
        <li>Eye brow enhancement</li>
        <li>Hot Towel Treatments</li>
        <li>Scalp | Blow outs | Shags</li>
        <li>Custom Design</li>
        <li>RazorCuts</li>
        <li>Shear Cuts</li>
        <li>Bobs | Perms | Relaxers</li>
        <li>Shoe Shine.</li>
      </ul>
    </div>
    <svg class="sweep" viewBox="0 0 480 300" preserveAspectRatio="none" aria-hidden="true">
      <path d="M480,40 C440,200 300,280 120,300 L480,300 Z" fill="var(--accent-violet)"/>
      <path d="M480,20 C430,190 290,270 100,300 L120,300 C300,280 440,200 480,40 Z" fill="var(--accent-violet-deep)"/>
    </svg>
  </section>
</body>
</html>
```